Lantern and Meadow Works: Problem to Solution Process

We need a powerpoint slide illustrating a process the begins with identifying a problem and proceed through various gates of potentially resolving the problem.
The attached file provides the steps a user must go through from point of recognizing they have a data need through resolving their problems are various stages.
This process is not yet in practice. It is a concept we are trying. We will use this slide to market the process while trying it with others.

Since the process is not yet in place, we need to visually communicate the theory we are implementing for users to quickly and easily understand. The resulting slide you are producing should tell the story of the user's path and the benefits for moving through this process. The slide with the process can include animation and / or videos to help demonstrate appropriately.
The largest benefit to the user is more immediate access to their data needs, to provide quicker insights and better decision making.
On the attached slide, the blue boxes are the processes we want to highlight. The text in the gray dotted boxes are intended to be informational for your purposes.
Each step 1- 4 should solve a user's problem. For example, if 100 problems are found, 50 should be resolved in step 1 and only 50 should move to step 2. Furthermore, only 30 should move to step 3 and 5 request should move to step 4. (Today, users go directly to step 4 for everything and it’s overwhelming to everyone!)

```html
<!DOCTYPE html>
<html lang="en">
<head>
<meta charset="utf-8">
<title>Lantern and Meadow Works: Problem to Solution Process</title>
<link href="https://fonts.googleapis.com/css2?family=Lato:ital,wght@0,400;0,700;1,400&display=swap" rel="stylesheet">
<style>
  :root {
    --page: #eef1f2;
    --slide: #1e2a32;
    --ink: #ffffff;
    --muted-ink: #f2f4f5;
    --role: #c9a65a;
    --step-a: #2a6c74;
    --step-b: #3d5a6c;
    --step-edge: #1c8b8f;
    --badge: #4d6d88;
    --start: #9be35a;
    --finish: #22b9d0;
    --flow: #7d6aa8;
    --branch: #8a5ad0;
    --alert: #e8506e;
    --note-edge: #5c6b73;
  }
  html, body {
    margin: 0;
    width: 1200px;
    height: 1060px;
    overflow: hidden;
    background: var(--page);
    font-family: "Lato", sans-serif;
  }
  .slide {
    position: absolute;
    left: 90px;
    top: 226px;
    width: 1020px;
    height: 566px;
    background: var(--slide);
    box-shadow: 0 24px 40px rgba(0,0,0,0.25);
  }
  .slide svg { display: block; }
  .note-frame { fill: none; stroke: var(--note-edge); stroke-width: 1.5; stroke-dasharray: 5 4; }
  .note-text { fill: var(--muted-ink); font-size: 16px; text-anchor: middle; }
  .step-shape { fill: url(#stepFill); stroke: var(--step-edge); stroke-width: 3; }
  .step-title { fill: var(--ink); font-size: 23px; font-weight: 700; text-anchor: middle; }
  .step-role { fill: var(--role); font-size: 21px; font-style: italic; text-anchor: middle; }
  .start-shape { fill: var(--slide); stroke: var(--start); stroke-width: 3.5; }
  .finish-shape { fill: var(--slide); stroke: var(--finish); stroke-width: 3.5; }
  .plain-text { fill: var(--ink); font-size: 23px; text-anchor: middle; }
  .badge circle { fill: var(--badge); stroke: #ffffff; stroke-width: 4; }
  .badge text { fill: #ffffff; font-size: 20px; font-weight: 700; text-anchor: middle; }
  .flow { fill: none; stroke: var(--flow); stroke-width: 3; stroke-dasharray: 7 5; }
  .branch { fill: none; stroke: var(--branch); stroke-width: 3; stroke-dasharray: 7 5; }
  .alert-line { fill: none; stroke: var(--alert); stroke-width: 3; stroke-dasharray: 12 7; }
  .alert-frame { fill: none; stroke: var(--alert); stroke-width: 3; stroke-dasharray: 12 7; }
  .flow-label { fill: var(--ink); font-size: 16px; }
  .branch-label { fill: var(--branch); font-size: 16px; }
  .alert-label { fill: var(--alert); font-size: 16px; }
</style>
</head>
<body>
<main class="slide">
<svg width="1020" height="566" viewBox="0 0 1738 965" aria-label="Lantern and Meadow Works problem to solution process">
  <defs>
    <linearGradient id="stepFill" x1="0" y1="0" x2="1" y2="1">
      <stop offset="0" stop-color="#2a6c74"/>
      <stop offset="1" stop-color="#3d5a6c"/>
    </linearGradient>
    <marker id="headFlow" viewBox="0 0 10 10" refX="8" refY="5" markerWidth="4" markerHeight="4" orient="auto"><path d="M0,0 L10,5 L0,10 Z" fill="#7d6aa8"/></marker>
    <marker id="headBranch" viewBox="0 0 10 10" refX="8" refY="5" markerWidth="4" markerHeight="4" orient="auto"><path d="M0,0 L10,5 L0,10 Z" fill="#8a5ad0"/></marker>
    <marker id="headAlert" viewBox="0 0 10 10" refX="8" refY="5" markerWidth="4" markerHeight="4" orient="auto"><path d="M0,0 L10,5 L0,10 Z" fill="#e8506e"/></marker>
  </defs>

  <!-- informational notes -->
  <g class="notes">
    <rect class="note-frame" x="455" y="139" width="291" height="200" rx="6"/>
    <text class="note-text"><tspan x="602" y="177">Goal is for majority of needs</tspan><tspan x="602" y="200">are resolved with Self service</tspan><tspan x="602" y="223">by the end user.</tspan></text>

    <rect class="note-frame" x="853" y="39" width="305" height="290" rx="6"/>
    <text class="note-text"><tspan x="1005" y="79">If the problem cannot by resolved</tspan><tspan x="1005" y="102">by themselves, then they connect</tspan><tspan x="1005" y="125">with a “super user” designation</tspan><tspan x="1005" y="149">within the business.  If they cannot</tspan><tspan x="1005" y="172">solve the problem, they need to</tspan><tspan x="1005" y="195">evaluate if it’s a large initiative or a</tspan><tspan x="1005" y="218">small initiative to resolve.</tspan></text>

    <rect class="note-frame" x="1298" y="89" width="297" height="240" rx="6"/>
    <text class="note-text"><tspan x="1446" y="127">The Business Intelligence team</tspan><tspan x="1446" y="150">works in Agile teams. If it is a</tspan><tspan x="1446" y="173">quick, small fix, then a user story</tspan><tspan x="1446" y="196">is created in the appropriate BI</tspan><tspan x="1446" y="219">team to quickly resolve it.</tspan></text>

    <rect class="note-frame" x="1286" y="700" width="284" height="195" rx="6"/>
    <text class="note-text"><tspan x="1428" y="810">If it is a large initiative to</tspan><tspan x="1428" y="833">resolve, then a problem solving</tspan><tspan x="1428" y="856">exercise needs to be completed</tspan><tspan x="1428" y="879">to define the problem.</tspan></text>

    <rect class="note-frame" x="853" y="700" width="295" height="227" rx="6"/>
    <text class="note-text"><tspan x="1001" y="812">Once the problem is understood, the</tspan><tspan x="1001" y="835">architecture design, data quality,</tspan><tspan x="1001" y="858">data consistency and plan of how to</tspan><tspan x="1001" y="882">solve the problem is created.</tspan><tspan x="1001" y="905">Once aligned it is then executed</tspan></text>

    <rect class="note-frame" x="434" y="700" width="301" height="192" rx="6"/>
    <text class="note-text"><tspan x="588" y="818">Regardless of the solution is resolved</tspan><tspan x="588" y="841">in steps 1, 2, 3, or 4, benefits and</tspan><tspan x="588" y="864">feedback is needed</tspan></text>

    <rect class="note-frame" x="36" y="700" width="282" height="203" rx="6"/>
    <text class="note-text"><tspan x="177" y="829">Reflection, feedback and training is</tspan><tspan x="177" y="855">needed to gain additional insights</tspan></text>
  </g>

  <!-- alert request note -->
  <rect class="alert-frame" x="1416" y="432" width="262" height="123" rx="10" fill="#1e2a32"/>
  <text class="note-text"><tspan x="1548" y="463">If the user needs data to finish</tspan><tspan x="1548" y="488">problem solving exercise, then a</tspan><tspan x="1548" y="513">request needs to be entered to</tspan><tspan x="1548" y="538">quickly provide the data.</tspan></text>

  <!-- connectors -->
  <path class="flow" d="M320,327 H448" marker-end="url(#headFlow)"/>
  <path class="flow" d="M748,327 H846" marker-end="url(#headFlow)"/>
  <path class="flow" d="M1155,327 H1292" marker-end="url(#headFlow)"/>
  <path class="branch" d="M1226,327 V586 H1428 V611" marker-end="url(#headBranch)"/>
  <path class="alert-line" d="M1570,698 H1690 V327 H1598" marker-end="url(#headAlert)"/>
  <path class="flow" d="M1284,693 H1154" marker-end="url(#headFlow)"/>
  <path class="flow" d="M851,693 H741" marker-end="url(#headFlow)"/>
  <path class="flow" d="M433,693 H324" marker-end="url(#headFlow)"/>
  <path class="flow" d="M178,608 V417" marker-end="url(#headFlow)"/>

  <text class="flow-label" text-anchor="middle"><tspan x="799" y="354">Results</tspan><tspan x="799" y="373">Not found</tspan></text>
  <text class="flow-label"><tspan x="1174" y="288">Existing, small</tspan><tspan x="1174" y="307">or Quick Fix</tspan></text>
  <text class="branch-label"><tspan x="1237" y="559">Larger</tspan><tspan x="1237" y="577">Initiative / New</tspan></text>
  <text class="alert-label"><tspan x="1581" y="725">Need more data</tspan><tspan x="1581" y="744">to define</tspan><tspan x="1581" y="764">problem</tspan></text>
  <text class="flow-label" text-anchor="middle"><tspan x="388" y="638">Train</tspan><tspan x="388" y="657">&amp;</tspan><tspan x="388" y="676">Adopt</tspan></text>

  <!-- start -->
  <path class="start-shape" d="M58,243 H282 L318,327 L282,410 H58 Q36,410 36,388 V265 Q36,243 58,243 Z"/>
  <text class="plain-text"><tspan x="166" y="304">User to communicate</tspan><tspan x="166" y="337">the problem they are</tspan><tspan x="166" y="369">trying to solve</tspan></text>

  <!-- step 1 -->
  <path class="step-shape" d="M475,243 H683 L723,327 L683,410 H475 Q453,410 453,388 V265 Q453,243 475,243 Z"/>
  <text class="step-title"><tspan x="584" y="299">Self</tspan><tspan x="584" y="330">Service</tspan></text>
  <text class="step-role" x="584" y="376">End User</text>
  <g class="badge"><circle cx="718" cy="327" r="28"/><text x="718" y="334">1</text></g>

  <!-- step 2 -->
  <path class="step-shape" d="M875,243 H1083 L1123,327 L1083,410 H875 Q853,410 853,388 V265 Q853,243 875,243 Z"/>
  <text class="step-title"><tspan x="987" y="284">Super User  Or</tspan><tspan x="987" y="314">Problem Definition</tspan><tspan x="987" y="345">Creation</tspan></text>
  <text class="step-role" x="987" y="389">Super User</text>
  <g class="badge"><circle cx="1125" cy="327" r="28"/><text x="1125" y="334">2</text></g>

  <!-- step 3 -->
  <path class="step-shape" d="M1320,243 H1523 L1563,327 L1523,410 H1320 Q1298,410 1298,388 V265 Q1298,243 1320,243 Z"/>
  <text class="step-title"><tspan x="1430" y="297">Worked within</tspan><tspan x="1430" y="329">Agile</tspan></text>
  <text class="step-role" x="1430" y="375">BI teams</text>
  <g class="badge"><circle cx="1564" cy="327" r="28"/><text x="1564" y="334">3</text></g>

  <!-- problem solving -->
  <rect class="step-shape" x="1286" y="615" width="284" height="168" rx="20"/>
  <text class="step-title"><tspan x="1428" y="676">Problem Solving to</tspan><tspan x="1428" y="708">Define problem</tspan></text>
  <text class="step-role" x="1428" y="754">Super User</text>

  <!-- step 4 -->
  <path class="step-shape" d="M893,615 H1126 Q1148,615 1148,637 V761 Q1148,783 1126,783 H893 L853,699 Z"/>
  <text class="step-title"><tspan x="1017" y="663">Project Design &amp;</tspan><tspan x="1017" y="695">Execute</tspan></text>
  <text class="step-role" x="1017" y="741">BI/EA teams</text>
  <g class="badge"><circle cx="883" cy="693" r="28"/><text x="883" y="700">4</text></g>

  <!-- step 5 -->
  <path class="step-shape" d="M475,608 H713 Q735,608 735,630 V755 Q735,777 713,777 H475 L435,693 Z"/>
  <text class="step-title" x="610" y="679">Check Benefits</text>
  <text class="step-role" x="610" y="726">BI teams</text>
  <g class="badge"><circle cx="463" cy="693" r="28"/><text x="463" y="700">5</text></g>

  <!-- outcome -->
  <rect class="finish-shape" x="36" y="610" width="282" height="167" rx="12"/>
  <text class="plain-text"><tspan x="176" y="680">Gain insights</tspan><tspan x="176" y="726">End User</tspan></text>
</svg>
</main>
</body>
</html>
```